Reef Glow

sunglasses, sihoullette of body, maybe wearing a bikini or sunglasses. I am offering spray tanning, body wraps, tanning beds, stand up, body art, airbrush makeup.

Target Market(s)

I would say my target is all ages, But tanning is a seasonal business and more beauty and aging concept. and around prom time I get my most profitable business. so 18 to 21 through march and april. then 25 to 55 through april to june.

Industry/Entity Type

Makeup

Contact Information for Business Card

Phone number: 701-382-5147 Owner: Jan Mortby (Lisowski)

Colors

Designer to choose colors to be used in the design.

Requirements
Nice to have
• Sunglasses, silouttes of body wearing sunglasses or bikini, or picture of spray gun.

```html
<!DOCTYPE html>
<html lang="en">
<head>
<meta charset="utf-8">
<title>Reef Glow – Business Card</title>
<link rel="stylesheet" href="https://fonts.googleapis.com/css2?family=Tinos:wght@400;700&display=swap">
<style>
  :root {
    --page: #ffffff;
    --card-light: #ffffff;
    --card-tan: #cfae78;
    --brand-brown: #5a3b20;
    --ink: #1f1a15;
    --accent-brown: #8a6647;
    --owner-brown: #5e4a38;
    --frame-brown: #8c7058;
    --frame-light: #e9dccd;
    --shadow: rgba(0, 0, 0, 0.28);
  }
  * { margin: 0; padding: 0; box-sizing: border-box; }
  html, body {
    width: 1200px;
    height: 800px;
    overflow: hidden;
    background: var(--page);
  }
  .canvas {
    position: relative;
    width: 1200px;
    height: 800px;
    font-family: "Tinos", "Times New Roman", serif;
  }
  .business-card {
    position: absolute;
    left: 195px;
    top: 100px;
    width: 893px;
    height: 548px;
    background: linear-gradient(212deg, var(--card-tan) 0%, #dcc39c 30%, #efe3d2 48%, var(--card-light) 62%);
    box-shadow: 6px -4px 8px var(--shadow);
  }
  .illustration-oval {
    position: absolute;
    left: 250px;
    top: 113px;
    width: 290px;
    height: 340px;
  }
  .spray-gun-art {
    position: absolute;
    left: 563px;
    top: 318px;
    width: 52px;
    height: 52px;
  }
  .brand-name {
    position: absolute;
    left: 628px;
    top: 182px;
    font-size: 68px;
    font-weight: 700;
    line-height: 1;
    color: var(--brand-brown);
    letter-spacing: 1px;
  }
  .owner-name {
    position: absolute;
    left: 663px;
    top: 390px;
    font-size: 33px;
    line-height: 1;
    color: var(--ink);
  }
  .owner-name .tone { color: var(--accent-brown); }
  .owner-title {
    position: absolute;
    left: 780px;
    top: 435px;
    font-size: 22px;
    line-height: 1;
    color: var(--owner-brown);
  }
  .contact-list {
    position: absolute;
    left: 252px;
    top: 484px;
    list-style: none;
    font-size: 25px;
    line-height: 30.5px;
    color: var(--ink);
  }
  .contact-list .value { color: var(--accent-brown); }
</style>
</head>
<body>
<main class="canvas">
  <section class="business-card" aria-label="Reef Glow business card"></section>

  <svg class="illustration-oval" viewBox="0 0 290 340" role="img" aria-label="Illustration of a slender body silhouette inside a tilted oval frame">
    <defs>
      <linearGradient id="oval-fill" x1="0" y1="0" x2="1" y2="1">
        <stop offset="0" stop-color="#b89c80"/>
        <stop offset="0.5" stop-color="#f3ebe2"/>
        <stop offset="1" stop-color="#8c7058"/>
      </linearGradient>
    </defs>
    <ellipse cx="145" cy="170" rx="118" ry="168" transform="rotate(22 145 170)" fill="url(#oval-fill)"/>
  </svg>

  <svg class="spray-gun-art" viewBox="0 0 52 52" role="img" aria-label="Small illustration of a spray tan gun">
    <rect x="0" y="0" width="52" height="52" rx="4" fill="#d8c3a0"/>
  </svg>

  <h1 class="brand-name">Reef Glow</h1>

  <p class="owner-name"><span class="tone">J</span>an <span class="tone">M</span>ortby <span class="tone">Lisow</span>ski</p>
  <p class="owner-title">Owner</p>

  <ul class="contact-list">
    <li>Coral <span class="value">Beach</span> 101</li>
    <li>Phone: <span class="value">701</span>-<span class="value">382</span>-5147</li>
    <li>Email: <span class="value">reefglow@</span>glowtanstudio.com</li>
    <li>Web: Glow<span class="value">tanstudio.com</span></li>
  </ul>
</main>
</body>
</html>
```